Design a corporate looking website for Harbourline Funding

Need design only WordPress mock up for Harbourline Funding who provides short term finance solutions to other businesses. We need a corporate looking website that depicts a trustworthy, Dynamic fast acting company.
Visit http://k7.pagelantern-demo.net/ for current mock up We need something like e this but not the same with a design that depicts corporate with more colour and images, needs to install trust and fast action. Please feel free to change the layout as I am not wedded to current design but am happy with what on the landing page.

Target Market(s)

Small to medium sized Businesses

Industry/Entity Type

Finance

Number of Pages Required

1 page

Font styles to use
Sans Serif

Requirements
Must have
• Design Landing pages in WordPress
• Visit http://k7.pagelantern-demo.net/ for current mock up need Layout like this but with a design that depicts corporate with more colour and images, needs to install trust and fast action. Please feel free to change the layout as I am not happy with current design but am wedded to what on the landing page.
Should not have
• any copyright material on it.

```html
<!DOCTYPE html>
<html lang="en">
<head>
<meta charset="utf-8">
<title>Harbourline Funding</title>
<link href="https://fonts.googleapis.com/css2?family=Open+Sans:wght@400;600;700&display=swap" rel="stylesheet">
<style>
:root{
  --blue:#0b9be0;
  --blue-soft:#3fa6dc;
  --green:#41a948;
  --red:#e8392b;
  --teal:#19a9c4;
  --ink:#2b2b2b;
  --text:#4a4a4a;
  --muted:#7a7a7a;
  --nav:#2f3237;
  --grey-band:#ececec;
  --strip:#e4e8ec;
  --btn-grey:#7c7f83;
  --btn-light:#e3e6e9;
  --line:#e2e2e2;
  --white:#ffffff;
}
*{box-sizing:border-box;margin:0;padding:0}
html,body{width:1200px;height:3041px;overflow:hidden}
body{position:relative;background:var(--white);font-family:"Open Sans",Arial,sans-serif;color:var(--text)}
.abs{position:absolute}

/* header */
.site-header{left:0;top:0;width:1200px;height:118px;background:var(--white)}
.brand{left:105px;top:34px;display:flex;align-items:center;gap:12px}
.brand-dot{width:34px;height:34px;border-radius:50%;background:var(--blue)}
.brand-name{font-size:27px;font-weight:700;color:#1e5fa5;letter-spacing:.2px}
.search{left:800px;top:36px;width:300px;height:46px;border:2px solid #dcdcdc;border-radius:6px;display:flex;align-items:center;justify-content:space-between;padding:0 14px 0 18px;font-size:13px;color:#9a9a9a}

.main-nav{left:0;top:118px;width:1200px;height:60px;background:var(--nav);display:flex;align-items:center;padding-left:93px;gap:0}
.main-nav a{font-size:11.5px;color:#e8e8e8;text-decoration:none;text-transform:uppercase;padding:0 12px;height:60px;line-height:60px;position:relative}
.main-nav a.active{color:var(--blue)}
.main-nav a.active::after{content:"";position:absolute;left:12px;right:12px;bottom:12px;height:2px;background:var(--blue)}

/* banner */
.banner{left:0;top:178px;width:1200px;height:120px;background:var(--blue)}
.banner-title{left:91px;top:26px;color:var(--white);font-size:25px;line-height:33px}
.banner-title strong{font-weight:600}
.banner-btn{left:940px;top:39px;width:160px;height:43px;border:2px solid var(--white);border-radius:5px;color:var(--white);font-size:11px;text-align:center;line-height:39px;text-transform:uppercase}
.banner-notch{left:168px;top:118px;width:0;height:0;border-left:11px solid transparent;border-right:11px solid transparent;border-top:13px solid var(--blue)}

.hero{left:0;top:298px;width:1200px;height:578px;background:linear-gradient(100deg,#dfe6ee 0%,#c9d2dc 22%,#7d7a84 40%,#4d4a4f 58%,#8a9c80 78%,#c8d4c2 100%)}

.thumbs{left:0;top:876px;width:1200px;height:124px;background:var(--strip)}
.thumb{top:10px;width:198px;height:98px}
.thumb.t1{left:172px;background:linear-gradient(120deg,#e8eef3,#c6b7a5)}
.thumb.t2{left:391px;background:linear-gradient(120deg,#39404f,#9aa2b0)}
.thumb.t3{left:610px;background:linear-gradient(120deg,#1e1e22,#8c8e7c)}
.thumb.t4{left:829px;background:linear-gradient(120deg,#c9d6c5,#4a4446);outline:3px solid var(--blue);outline-offset:-1px}
.arrow{top:46px}

/* about */
.about-kicker{left:0;top:1040px;width:1200px;text-align:center;color:var(--blue);font-size:27px}
.about-title{left:0;top:1082px;width:1200px;text-align:center;color:var(--ink);font-size:32px}
.about-lead{left:200px;top:1150px;width:800px;text-align:center;font-size:12.5px;line-height:20px;color:var(--text)}
.divider{left:96px;top:1232px;width:1006px;height:2px;background:var(--line)}

.service{top:1272px;width:330px}
.service-icon{left:0;top:0;width:60px;height:60px;border-radius:50%;display:flex;align-items:center;justify-content:center}
.service h3{left:86px;top:6px;font-size:14.5px;font-weight:600;color:var(--ink);white-space:nowrap}
.service .rule{left:86px;top:40px;width:230px;height:1px;background:var(--line)}
.service p{left:86px;top:54px;width:232px;font-size:12px;line-height:19px;color:var(--text)}
.service .btn{left:86px;top:208px}
.btn{position:absolute;height:40px;padding:0 26px;line-height:40px;font-size:12px;border-radius:3px;white-space:nowrap}
.btn-light{background:var(--btn-light);color:#555;border:1px solid #d2d6da}
.btn-dark{background:var(--btn-grey);color:var(--white)}
.btn-blue{background:var(--blue-soft);color:var(--white)}

.dots{left:567px;top:1578px;display:flex;gap:6px}
.dots span{width:10px;height:10px;border-radius:50%;background:#d6d6d6}
.dots span.on{background:#9a9a9a}

/* why */
.why{left:0;top:1646px;width:1200px;height:385px;background:var(--grey-band)}
.why-photo{left:101px;top:57px;width:469px;height:267px;background:linear-gradient(120deg,#1d3f8f 0%,#2a5bb8 35%,#c9b8a6 60%,#2450a8 100%)}
.why h2{left:616px;top:62px;font-size:33px;font-weight:400;color:var(--ink)}
.why p{left:616px;top:118px;width:484px;font-size:12.5px;line-height:20.5px;color:var(--text)}
.why .btn{top:276px;height:40px}

/* steps */
.steps-title{left:0;top:2068px;width:1200px;text-align:center;font-size:33px;color:var(--ink)}
.step-circle{border-radius:50%;background:var(--white);display:flex;align-items:center;justify-content:center;font-size:58px;font-weight:400}
.step-bar{height:53px;color:var(--white);font-size:15px;text-align:center;line-height:53px}
.steps-note{left:0;top:2414px;width:1200px;text-align:center;font-size:12.5px;color:var(--text)}

/* testimonial */
.testimonials{left:0;top:2554px;width:1200px;height:379px;background:var(--blue)}
.testimonial-photo{left:470px;top:0;width:730px;height:379px;background:linear-gradient(180deg,#dbe6ef 0%,#b8c6d2 40%,#3c4550 70%,#8d98a3 100%)}
.quote-card{left:97px;top:57px;width:659px;height:263px;background:var(--white)}
.quote-card h2{left:48px;top:48px;font-size:20px;font-weight:600;color:var(--blue-soft)}
.quote-card blockquote{left:48px;top:118px;width:560px;font-size:12px;line-height:21px;font-style:italic;color:var(--text)}
.quote-card cite{left:0;top:196px;width:610px;text-align:right;font-style:normal;font-size:17px;color:var(--green)}

/* footer */
.site-footer{left:0;top:2933px;width:1200px;height:108px;background:var(--white)}
.site-footer .brand{top:36px}
.copyright{left:800px;top:48px;width:302px;text-align:right;font-size:12.5px;color:var(--ink)}
</style>
</head>
<body>

<header class="site-header abs">
  <div class="brand abs"><span class="brand-dot"></span><span class="brand-name">Harbourline Funding</span></div>
  <div class="search abs"><span>Search</span>
    <svg width="16" height="16" viewBox="0 0 16 16"><circle cx="6.5" cy="6.5" r="5" fill="none" stroke="#333" stroke-width="2"/><line x1="10" y1="10" x2="15" y2="15" stroke="#333" stroke-width="2"/></svg>
  </div>
</header>

<nav class="main-nav abs">
  <a class="active">Home</a><a>Services</a><a>Why Harbourline</a><a>Investors</a><a>About Us</a><a>Contact Us</a><a>Members Login</a>
</nav>

<section class="banner abs">
  <div class="banner-title abs">Business Taken<br>to The <strong>New Heights</strong></div>
  <div class="banner-btn abs">Read More</div>
</section>
<div class="banner-notch abs"></div>

<div class="hero abs" role="img" aria-label="Smiling woman placing banknotes into her wallet outdoors"></div>

<div class="thumbs abs">
  <svg class="arrow abs" style="left:96px" width="26" height="22" viewBox="0 0 26 22"><path d="M24 11H4M12 3 4 11l8 8" fill="none" stroke="#1b8fd6" stroke-width="3"/></svg>
  <div class="thumb t1 abs" role="img" aria-label="Woman holding a fan of banknotes"></div>
  <div class="thumb t2 abs" role="img" aria-label="Businessman holding a piggy bank"></div>
  <div class="thumb t3 abs" role="img" aria-label="Hands exchanging cash"></div>
  <div class="thumb t4 abs" role="img" aria-label="Woman counting money from her wallet"></div>
  <svg class="arrow abs" style="left:1076px" width="26" height="22" viewBox="0 0 26 22"><path d="M2 11h20M14 3l8 8-8 8" fill="none" stroke="#1b8fd6" stroke-width="3"/></svg>
</div>

<div class="about-kicker abs">About us</div>
<h1 class="about-title abs" style="font-weight:400">Present yourself to the whole world</h1>
<p class="about-lead abs">Contrary to popular belief, Lorem Ipsum is not simply random text. It has roots in a piece of classical Latin literature from 45 BC, making it over 2000 years old. Ellis Warden, a Latin professor at Fernhill College in Vermont</p>
<div class="divider abs"></div>

<article class="service abs" style="left:98px">
  <div class="service-icon abs" style="background:var(--teal)">
    <svg width="28" height="26" viewBox="0 0 28 26"><path d="M3 12 14 3l11 9M6 10v13h16V10" fill="none" stroke="#fff" stroke-width="2.5"/><rect x="11" y="15" width="6" height="8" fill="#fff"/></svg>
  </div>
  <h3 class="abs">Residential Real Estate Agents</h3>
  <div class="rule abs"></div>
  <p class="abs">Whether you're a Residential Real Estate Agency or Agent we understand that with residential real estate transactions settling on average in 42 days that your well earned and outstanding commissions ...</p>
  <span class="btn btn-light">Read More</span>
</article>

<article class="service abs" style="left:440px">
  <div class="service-icon abs" style="background:var(--green)">
    <svg width="30" height="30" viewBox="0 0 30 30"><circle cx="15" cy="15" r="5" fill="#fff"/><g stroke="#fff" stroke-width="2.5" stroke-linecap="round"><line x1="15" y1="2" x2="15" y2="6"/><line x1="15" y1="24" x2="15" y2="28"/><line x1="2" y1="15" x2="6" y2="15"/><line x1="24" y1="15" x2="28" y2="15"/><line x1="6" y1="6" x2="8.5" y2="8.5"/><line x1="21.5" y1="21.5" x2="24" y2="24"/><line x1="24" y1="6" x2="21.5" y2="8.5"/><line x1="8.5" y1="21.5" x2="6" y2="24"/></g></svg>
  </div>
  <h3 class="abs">Commercial Real Estate Agents</h3>
  <div class="rule abs"></div>
  <p class="abs">Whether you're a Commercial Real Estate Agency or Agent we understand that with commercial real estate transactions settling at all different periods that your well earned and outstanding commissions ...</p>
  <span class="btn btn-dark">Read More</span>
</article>

<article class="service abs" style="left:783px">
  <div class="service-icon abs" style="background:var(--red)">
    <svg width="26" height="26" viewBox="0 0 26 26"><g fill="none" stroke="#fff" stroke-width="2.5"><ellipse cx="13" cy="6" rx="9" ry="3.5"/><path d="M4 6v14c0 2 4 3.5 9 3.5s9-1.5 9-3.5V6M4 13c0 2 4 3.5 9 3.5s9-1.5 9-3.5"/></g></svg>
  </div>
  <h3 class="abs">Mortgage &amp; Finance Brokers</h3>
  <div class="rule abs"></div>
  <p class="abs">Whether you're a mortgage broker focusing on home loans or a finance broker operating in different area's of finance we have a deep understanding of your industry and the nuances involved, especially ...</p>
  <span class="btn btn-light">Read More</span>
</article>

<div class="dots abs"><span></span><span></span><span class="on"></span><span></span></div>

<section class="why abs">
  <div class="why-photo abs" role="img" aria-label="Hand holding a coin in front of a waving blue flag"></div>
  <h2 class="abs">Why Harbourline Funding</h2>
  <p class="abs">At Harbourline Funding our aim is to provide immediate commission advance solutions for all industries. Our background is sales, property and finance and we understand the issues faced with Small to medium Businesses, Agents, contractors and consultants who earn commissions. Unforeseen expenses, inconstant sales, holiday periods, sickness, taxation bills and job changes can all have an effect on a sales and commission flow.</p>
  <span class="btn btn-dark" style="left:614px">Read More</span>
  <span class="btn btn-blue" style="left:742px">Our Pricing Guaranteed</span>
  <span class="btn btn-dark" style="left:929px;padding:0 27px">Our Loyalty Program</span>
</section>

<h2 class="steps-title abs" style="font-weight:400">3 Easy Steps To a Stress Free Solution</h2>

<div class="step-circle abs" style="left:172px;top:2183px;width:166px;height:166px;border:6px solid var(--blue-soft);color:var(--blue-soft)">01</div>
<div class="step-bar abs" style="left:99px;top:2319px;width:317px;background:var(--blue-soft)">Call or click</div>

<div class="step-circle abs" style="left:514px;top:2148px;width:176px;height:176px;border:7px solid var(--green);color:var(--green)">02</div>
<div class="step-bar abs" style="left:440px;top:2321px;width:316px;background:var(--green);border:2px solid #2f8e37;line-height:49px">Fill out &amp; Sign</div>

<div class="step-circle abs" style="left:860px;top:2183px;width:166px;height:166px;border:6px solid var(--blue-soft);color:var(--blue-soft)">03</div>
<div class="step-bar abs" style="left:785px;top:2319px;width:316px;background:var(--blue-soft)">Funds in bank in 4 hours</div>

<p class="steps-note abs">A hassle free finance solution that grows as your business grows</p>
<span class="btn btn-dark" style="left:543px;top:2463px;width:116px;padding:0;text-align:center;height:38px;line-height:38px">Start Now</span>

<section class="testimonials abs">
  <div class="testimonial-photo abs" role="img" aria-label="Silhouetted business team talking by a bright office window"></div>
  <div class="quote-card abs">
    <h2 class="abs">What people say about us</h2>
    <blockquote class="abs">" The service was beyond my expectations. But please, replace this with an actual customer testimonial, this is just for testing purposes ".</blockquote>
    <cite class="abs">Dana Whitfield, Bright Mornings LLC</cite>
  </div>
</section>

<footer class="site-footer abs">
  <div class="brand abs"><span class="brand-dot" style="background:#8a8f96"></span><span class="brand-name" style="color:#5f646b">Harbourline Funding</span></div>
  <div class="copyright abs">Copyright © 2016, All Right Reserved</div>
</footer>

</body>
</html>
```